Musician Business Card Design

I am freelance Double Bass player based in New York. I play every style of music, from Pop music to Contemporary Classical Music. I am also a private Bass and music theory teacher. What I hope to communicate with my business card is that I am a reliable and competent musician. I like designs with geometric patterns, I am very found of mandalas, so maybe we could incorporate that into the idea. I am looking for a design that will be easy on the eyes, and will have something that will make people want to keep it.
Thanks for all your help.

Industry/Entity Type

Business

Contact Information for Business Card

Tomas Verrault
+1 (347) 555-0182
okafor.tm@quillnest.com

```html
<!DOCTYPE html>
<html lang="en">
<head>
<meta charset="utf-8">
<title>Tomas Verrault — Business Card</title>
<link rel="stylesheet" href="https://fonts.googleapis.com/css2?family=Federo&family=Poiret+One&display=swap">
<style>
  :root {
    --page: #e8e5df;
    --card: #0a0c0b;
    --teal-bright: #43b3a9;
    --teal-mid: #1f6d67;
    --teal-deep: #0f3431;
    --teal-night: #0b1c1a;
    --shadow: rgba(0, 0, 0, 0.3);
  }
  * { margin: 0; padding: 0; box-sizing: border-box; }
  html, body {
    width: 1200px;
    height: 1200px;
    overflow: hidden;
    background: var(--page);
  }
  .sheet {
    position: relative;
    width: 1200px;
    height: 1200px;
  }
  .card {
    position: absolute;
    left: 180px;
    width: 840px;
    height: 480px;
    background: var(--card);
    overflow: hidden;
    box-shadow: 0 10px 26px var(--shadow);
  }
  .card--front { top: 90px; }
  .card--back { top: 630px; }

  .mandala-panel {
    position: absolute;
    left: 0;
    top: 0;
    width: 270px;
    height: 305px;
    background: radial-gradient(circle at 40% 55%, #1c3431 0%, #12211f 45%, #0d1413 75%, var(--card) 100%);
    border-right: 1px solid #1a2624;
  }
  .ornament-strip {
    position: absolute;
    left: 0;
    right: 0;
    top: 30px;
    height: 40px;
    background: linear-gradient(90deg, #1a4f4a, #2a7f77 30%, #236d66 60%, #1a4f4a);
    border-top: 1px solid var(--teal-bright);
    border-bottom: 1px solid var(--teal-bright);
  }
  .mandala-band {
    position: absolute;
    left: 0;
    right: 0;
    bottom: 0;
    height: 175px;
    background: linear-gradient(90deg,
      var(--teal-night) 0%, #1d5a54 10%, var(--teal-night) 20%,
      #1d5a54 30%, var(--teal-night) 40%, #1d5a54 50%,
      var(--teal-night) 60%, #1d5a54 70%, var(--teal-night) 80%,
      #1d5a54 90%, var(--teal-night) 100%);
    border-top: 2px solid var(--teal-mid);
  }

  .card-name {
    position: absolute;
    right: 30px;
    top: 82px;
    font-family: "Federo", sans-serif;
    font-size: 56px;
    font-weight: 400;
    line-height: 1;
    color: var(--teal-bright);
  }
  .card-contact {
    position: absolute;
    right: 30px;
    bottom: 186px;
    font-family: "Poiret One", sans-serif;
    font-size: 28px;
    line-height: 1.2;
    color: var(--teal-bright);
    list-style: none;
  }
</style>
</head>
<body>
<main class="sheet">
  <section class="card card--front" aria-label="Business card front">
    <div class="mandala-panel" role="img" aria-label="Large faint teal mandala line pattern"></div>
    <div class="ornament-strip" role="img" aria-label="Teal geometric ornament border"></div>
    <h1 class="card-name">Tomas Verrault</h1>
    <div class="mandala-band" role="img" aria-label="Row of five teal line mandalas"></div>
  </section>

  <section class="card card--back" aria-label="Business card back">
    <div class="mandala-panel" role="img" aria-label="Large faint teal mandala line pattern"></div>
    <div class="ornament-strip" role="img" aria-label="Teal geometric ornament border"></div>
    <ul class="card-contact">
      <li class="card-contact__email">okafor.tm@quillnest.com</li>
      <li class="card-contact__phone">+1 (347) 555-0182</li>
    </ul>
    <div class="mandala-band" role="img" aria-label="Row of five teal line mandalas"></div>
  </section>
</main>
</body>
</html>
```